Powerpoint template design for Oil and Gas Investment Fund Pitchdeck

I need a template design for an oil and gas investment fund pitch deck. Design needs to be clean and have plenty of space for inserting graphics. Audience is high net worth individuals and corporate finance executives (private equity firms). We will need a title page with our logo and some oil& gas images (some included already) and the template for the internal pages. A rough example is attached. I would like to keep the current page dimensions because we have many financial charts we will want to add to the template pages. So the template will need to include title page, internal page, and a team page.

Target Market(s)

High etw worth individual investors and corporate finance professionals

Industry/Entity Type

Oil an dgas investment fund

Font styles to use
Serif

Requirements
Must have
• title page, interior page, team page

```html
<!DOCTYPE html>
<html lang="en">
<head>
<meta charset="utf-8">
<title>Harrow Ridge Business Presentation – Template Overview</title>
<link rel="stylesheet" href="https://fonts.googleapis.com/css2?family=Roboto+Condensed:wght@300;400;700&family=Roboto:wght@300;400;700&display=swap">
<style>
:root{
  --ink:#2b2b2b;
  --text:#555;
  --muted:#9a9a9a;
  --rule:#cfcfcf;
  --band:#e4e4e4;
  --paper:#ffffff;
  --dark:#333333;
  --mid:#8a8a8a;
  --light:#d8d8d8;
}
*{margin:0;padding:0;box-sizing:border-box}
html,body{width:975px;height:1200px;overflow:hidden;background:var(--paper)}
body{font-family:'Roboto',Arial,sans-serif;color:var(--ink)}
.deck{display:grid;grid-template-columns:repeat(3,287px);column-gap:24px;row-gap:31px;padding:36px 29px}
.slide{position:relative;width:287px;height:161px;background:var(--paper);overflow:hidden;box-shadow:0 6px 14px rgba(0,0,0,.28)}
.slide > *{position:absolute}
.accent{left:22px;top:6px;width:46px;height:1px;background:linear-gradient(90deg,#222 55%,#c4c4c4)}
.title{left:21px;top:11px;font:300 12.5px/1.1 'Roboto Condensed',Arial,sans-serif;color:var(--ink);white-space:nowrap}
.subhead{left:21px;top:27px;font:400 2.6px 'Roboto',sans-serif;color:var(--muted);text-transform:uppercase;letter-spacing:.05px}
.footer{left:0;bottom:0;width:100%;height:9px;background:var(--band)}
.footer-note{left:20px;bottom:3px;font:2.6px 'Roboto',sans-serif;color:var(--muted)}
.footer-brand{right:17px;bottom:2px;display:flex;align-items:center;gap:1px;font:700 2.3px 'Roboto Condensed',sans-serif;color:var(--dark);letter-spacing:.1px}
.footer-brand i{display:block;width:3px;height:3px;background:var(--dark)}
.copy{font:300 2.7px/4px 'Roboto',sans-serif;color:var(--text);text-align:justify}
.copy p{margin-bottom:1.5px}
.copy b{font-weight:400;color:var(--ink)}
.photo{background:linear-gradient(180deg,#2c2c2c,#6d6d6d 60%,#a9a9a9)}

/* title slides */
.cover-hero{left:0;top:0;width:100%;height:100%;background:linear-gradient(180deg,#353535 0%,#4a4a4a 55%,#8d8d8d 100%)}
.cover-frames{left:8px;top:19px;width:271px;height:95px;display:flex;gap:1px}
.cover-frames span{flex:1;border:.6px solid rgba(255,255,255,.45);background:linear-gradient(180deg,rgba(0,0,0,.25),rgba(255,255,255,.08))}
.cover-title{left:0;top:118px;width:100%;text-align:center;font:300 12px 'Roboto Condensed',sans-serif;color:#fff}
.cover-sub{left:0;top:133px;width:100%;text-align:center;font:300 7px 'Roboto Condensed',sans-serif;color:#eee}
.conf{font:400 3px 'Roboto Condensed',sans-serif;color:#fff;letter-spacing:.1px}
.hero-band{left:0;top:0;width:100%;height:16px;background:#262626}
.hero-photo{left:0;top:16px;width:100%;height:145px;background:linear-gradient(100deg,#1f1f1f 0%,#555 45%,#9b9b9b 100%)}
.hero-title{left:203px;top:52px;font:300 11px/13.5px 'Roboto Condensed',sans-serif;color:#fff}
.hero-sub{left:209px;top:96px;font:300 5px/7px 'Roboto Condensed',sans-serif;color:#eee;text-align:center}

/* agenda */
.agenda-list{left:100px;top:47px;display:grid;grid-template-columns:74px 74px;row-gap:8.4px}
.agenda-item{display:flex;align-items:center;font:3.6px 'Roboto',sans-serif;color:var(--ink);height:6px}
.agenda-item em{font-style:normal;font-size:4.4px;width:8px}
.agenda-item span{border-left:.5px solid var(--rule);padding-left:3px;height:9px;line-height:9px}

/* team */
.member{top:43px;width:66px;text-align:center}
.member .portrait{width:66px;height:42px;border-radius:2px;background:linear-gradient(180deg,#4a3a30,#7d6f66 55%,#2d2d2d)}
.member h3{font:400 5.2px 'Roboto Condensed',sans-serif;margin-top:3px;color:var(--ink)}
.member h4{font:300 2.6px 'Roboto',sans-serif;color:var(--muted);margin-bottom:5px}
.member p{font:300 2.6px/3.6px 'Roboto',sans-serif;color:var(--muted);text-align:justify;padding:0 3px}

/* bullets */
.icon-item{width:70px;text-align:center}
.icon-item svg{display:block;margin:0 auto 2px}
.icon-item h3,.num-item h3{font:400 5.5px 'Roboto Condensed',sans-serif;color:var(--ink)}
.icon-item p{font:300 2.6px/3.6px 'Roboto',sans-serif;color:var(--text);margin-top:2px}
.num-item{width:78px}
.num-item h3 em{font-style:normal;font-size:7px;margin-right:3px}
.num-item p{font:300 2.6px/3.6px 'Roboto',sans-serif;color:var(--muted);margin:5px 0 0 12px}

/* options */
.option{top:47px;width:52px;height:78px;border:.6px solid var(--rule);padding:4px 5px}
.option strong{display:block;font:300 11px 'Roboto Condensed',sans-serif;color:var(--ink)}
.option.dim strong{color:var(--muted)}
.option p{font:300 2.8px/4px 'Roboto',sans-serif;color:var(--text);margin-top:3px}
.option-btn{top:126px;width:52px;height:9px;background:#999;color:#fff;font:300 4.6px/9px 'Roboto Condensed',sans-serif;text-align:center}
.option-btn.on{background:var(--dark)}

/* data */
.list-item{display:flex;gap:5px;align-items:flex-start;margin-top:3px}
.list-item em{font-style:normal;font:400 6px/6px 'Roboto Condensed',sans-serif;color:var(--ink);width:5px}
.list-item p{font:300 2.6px/3.4px 'Roboto',sans-serif;color:var(--text)}
.chart-label{font:2.6px 'Roboto',sans-serif;fill:#777}
</style>
</head>
<body>
<main class="deck">

<!-- 1 Cover -->
<section class="slide">
  <div class="cover-hero photo" role="img" aria-label="Oil drilling rig silhouette at dusk, black and white"></div>
  <div class="cover-frames"><span></span><span></span><span></span><span></span><span></span></div>
  <h1 class="cover-title">Harrow Ridge Business Presentation</h1>
  <p class="cover-sub">Your subtitle presentation goes here</p>
  <p class="conf" style="left:0;width:100%;text-align:center;top:150px">PRIVATE AND CONFIDENTIAL</p>
</section>

<!-- 2 Cover alt -->
<section class="slide">
  <div class="hero-band"></div>
  <div class="hero-photo" role="img" aria-label="Drilling derrick against a grey sky, black and white"></div>
  <h1 class="hero-title">Harrow Ridge<br>Business<br>Presentation</h1>
  <p class="hero-sub">Your subtitle<br>presentation goes here</p>
  <p class="conf" style="left:212px;top:141px">PRIVATE AND CONFIDENTIAL</p>
</section>

<!-- 3 Cover alt white -->
<section class="slide">
  <div class="accent"></div>
  <div class="hero-photo" style="height:131px" role="img" aria-label="Drilling derrick against a grey sky, black and white"></div>
  <h1 class="hero-title">Harrow Ridge<br>Business<br>Presentation</h1>
  <p class="hero-sub">Your subtitle<br>presentation goes here</p>
  <p class="conf" style="left:212px;top:139px">PRIVATE AND CONFIDENTIAL</p>
</section>

<!-- 4 Disclaimer -->
<section class="slide">
  <div class="accent"></div>
  <h2 class="title" style="top:62px">Disclaimer</h2>
  <p class="copy" style="left:21px;top:88px;width:245px;font-size:4.5px;line-height:5.6px;color:#222;font-weight:400">Nothing contained in these documents and materials is meant to be, and shall not be considered, a security offering, an offer to invest, or a solicitation of funds for any purpose. All information contained in these materials and documents, including, but not limited to, numbers, dollar amounts, rates of return, oil production, projections, etc. are included in such materials and documents purely for informational and discussion purposes only, and are strictly conjecture. The success of this proposed business idea or venture is not guaranteed in any way, and any investment in such business idea or venture carries the risk of significant or complete loss of investment.</p>
  <div class="footer"></div><p class="footer-note">Page: 4 &nbsp;|&nbsp; Harrow Ridge presentation to: Company Investor</p><p class="footer-brand"><i></i>HARROW RIDGE</p>
</section>

<!-- 5 Welcome -->
<section class="slide">
  <div class="accent"></div>
  <h2 class="title" style="left:24px;top:45px;white-space:normal;width:60px">Welcome message</h2>
  <div class="copy" style="left:87px;top:47px;width:177px;font-size:3px;line-height:4.3px">
    <p>Our fund acquires producing oil and gas assets with steady cash flow and low decline rates. We partner with trusted operators to improve field efficiency and return capital to investors through quarterly distributions.</p>
    <p>Our fund acquires producing oil and gas assets with steady cash flow and low decline rates. We partner with trusted operators to improve field efficiency and return capital to investors through quarterly distributions.</p>
  </div>
  <div class="footer"></div><p class="footer-note">Page: 5 &nbsp;|&nbsp; Harrow Ridge presentation to: Company Investor</p><p class="footer-brand"><i></i>HARROW RIDGE</p>
</section>

<!-- 6 Agenda -->
<section class="slide">
  <div class="accent"></div>
  <h2 class="title" style="left:24px;top:49px">Agenda</h2>
  <p class="subhead" style="left:24px;top:64px;font-size:4.6px;text-transform:none;color:var(--text)">may 23 2022</p>
  <div class="agenda-list">
    <p class="agenda-item"><em>01</em><span>Welcome</span></p><p class="agenda-item"><em>07</em><span>Case of Study 1</span></p>
    <p class="agenda-item"><em>02</em><span>About Harrow Ridge</span></p><p class="agenda-item"><em>08</em><span>Case of Study 2</span></p>
    <p class="agenda-item"><em>03</em><span>What we Do</span></p><p class="agenda-item"><em>09</em><span>Case of Study 3</span></p>
    <p class="agenda-item"><em>04</em><span>Our Experience</span></p><p class="agenda-item"><em>10</em><span>Consultations</span></p>
    <p class="agenda-item"><em>05</em><span>Our projects</span></p><p class="agenda-item"><em>11</em><span>Conclusions</span></p>
    <p class="agenda-item"><em>06</em><span>Results</span></p><p class="agenda-item"><em>12</em><span>Questions</span></p>
  </div>
  <div class="footer"></div><p class="footer-note">Page: 6 &nbsp;|&nbsp; Harrow Ridge presentation to: Company Investor</p><p class="footer-brand"><i></i>HARROW RIDGE</p>
</section>

<!-- 7 Industry -->
<section class="slide">
  <div class="accent"></div>
  <h2 class="title">The Industry Today</h2>
  <p style="left:24px;top:39px;width:95px;font:300 6.8px/10px 'Roboto Condensed',sans-serif;color:#111">Typical “Major” O&amp;G Companies have thousands of horizontal wells and thousands of vertical wells. They want to focus on horizontal.</p>
  <div style="left:131px;top:37px;width:135px;height:97px;background:radial-gradient(circle at 45% 20%,#d8dcf0 0,#5a64a8 10%,#1b1f55 45%,#0a0c2a 80%),#0a0c2a" role="img" aria-label="Lit drilling rig at night under a full moon"></div>
  <div style="left:22px;top:106px;width:132px;height:25px;background:#dadada;box-shadow:0 1px 2px rgba(0,0,0,.25);display:flex;align-items:center;justify-content:center;text-align:center;padding:0 14px;font:300 4.3px/5.4px 'Roboto',sans-serif;color:#111">Strong economic motivation to divest Vertical wells on good terms to trusted operators like Harrow Ridge/HRC.</div>
  <div class="footer"></div><p class="footer-note">Page: 7 &nbsp;|&nbsp; Harrow Ridge presentation to: Company Investor</p><p class="footer-brand"><i></i>HARROW RIDGE</p>
</section>

<!-- 8 Images -->
<section class="slide">
  <div class="accent"></div>
  <h2 class="title">Images from operational areas &amp; descriptive text</h2>
  <p class="subhead">Lorem ipsum, giving information on its origins, as well as a random text here</p>
  <div style="left:22px;top:36px;width:106px;height:105px;background:radial-gradient(circle at 40% 45%,#4a8a3a,#6f5aa0 50%,#c9b85a 85%)" role="img" aria-label="Satellite view of a river delta in the operating area"></div>
  <div class="copy" style="left:141px;top:40px;width:122px">
    <p><b>Our assets</b></p>
    <p>Our fund acquires producing oil and gas assets with steady cash flow and low decline rates. We partner with trusted operators to improve field efficiency and return capital to investors through quarterly distributions. Our fund acquires producing oil and gas assets with steady cash flow and low decline rates. We partner with trusted operators to improve field efficiency and return capital to investors through quarterly distributions.</p>
    <p><b>Our approach</b></p>
    <p>Our fund acquires producing oil and gas assets with steady cash flow and low decline rates. We partner with trusted operators to improve field efficiency and return capital to investors through quarterly distributions.</p>
  </div>
  <div class="footer"></div><p class="footer-note">Page: 8 &nbsp;|&nbsp; Harrow Ridge presentation to: Company Investor</p><p class="footer-brand"><i></i>HARROW RIDGE</p>
</section>

<!-- 9 Team -->
<section class="slide">
  <div class="accent"></div>
  <h2 class="title">Team Slide</h2>
  <p class="subhead">Lorem ipsum, giving information on its origins, as well as a random text here</p>
  <div class="member" style="left:29px"><div class="portrait" role="img" aria-label="Portrait photo of a team member"></div><h3>Dale Whitcomb</h3><h4>Managing Partner</h4><p>Decades of field operations and asset management experience.</p></div>
  <div class="member" style="left:108px"><div class="portrait" role="img" aria-label="Portrait photo of a team member"></div><h3>Owen Prescott</h3><h4>Managing Partner</h4><p>Decades of field operations and asset management experience.</p></div>
  <div class="member" style="left:187px"><div class="portrait" style="background:linear-gradient(180deg,#c9ced4,#8a8e93 60%,#6d6256)" role="img" aria-label="Portrait photo of a team member in a hard hat"></div><h3>Lyle Brandt</h3><h4>Operations Manager</h4><p>Decades of field operations and asset management experience.</p></div>
  <div class="footer"></div><p class="footer-note">Page: 9 &nbsp;|&nbsp; Harrow Ridge presentation to: Company Investor</p><p class="footer-brand"><i></i>HARROW RIDGE</p>
</section>

<!-- 10 One column -->
<section class="slide">
  <div class="accent"></div>
  <h2 class="title">Text in One Column With Sub Header</h2>
  <p class="subhead">Lorem ipsum, giving information on its origins, as well as a random text here</p>
  <div class="copy" style="left:21px;top:35px;width:245px">
    <p>Our fund acquires producing oil and gas assets with steady cash flow and low decline rates. We partner with trusted operators to improve field efficiency and return capital to investors through quarterly distributions. Our fund acquires producing oil and gas assets with steady cash flow and low decline rates. We partner with trusted operators to improve field efficiency and return capital to investors through quarterly distributions.</p>
    <p>Our fund acquires producing oil and gas assets with steady cash flow and low decline rates. We partner with trusted operators to improve field efficiency and return capital to investors through quarterly distributions. Our fund acquires producing oil and gas assets with steady cash flow and low decline rates. We partner with trusted operators to improve field efficiency and return capital to investors through quarterly distributions.</p>
    <p>Our fund acquires producing oil and gas assets with steady cash flow and low decline rates. We partner with trusted operators to improve field efficiency and return capital to investors through quarterly distributions. Our fund acquires producing oil and gas assets with steady cash flow and low decline rates. We partner with trusted operators to improve field efficiency and return capital to investors through quarterly distributions.</p>
    <p>Our fund acquires producing oil and gas assets with steady cash flow and low decline rates. We partner with trusted operators to improve field efficiency and return capital to investors through quarterly distributions. Our fund acquires producing oil and gas assets with steady cash flow and low decline rates. We partner with trusted operators to improve field efficiency and return capital to investors through quarterly distributions.</p>
  </div>
  <div class="footer"></div><p class="footer-note">Page: 10 &nbsp;|&nbsp; Harrow Ridge presentation to: Company Investor</p><p class="footer-brand"><i></i>HARROW RIDGE</p>
</section>

<!-- 11 Two columns -->
<section class="slide">
  <div class="accent"></div>
  <h2 class="title">Text Slide in Two Columns With Sub Header</h2>
  <p class="subhead">Lorem ipsum, giving information on its origins, as well as a random text here</p>
  <div class="copy" style="left:21px;top:35px;width:117px">
    <p>Our fund acquires producing oil and gas assets with steady cash flow and low decline rates. We partner with trusted operators to improve field efficiency and return capital to investors through quarterly distributions. Our fund acquires producing oil and gas assets with steady cash flow and low decline rates. We partner with trusted operators to improve field efficiency and return capital to investors through quarterly distributions.</p>
    <p>Our fund acquires producing oil and gas assets with steady cash flow and low decline rates. We partner with trusted operators to improve field efficiency and return capital to investors through quarterly distributions. Our fund acquires producing oil and gas assets with steady cash flow and low decline rates. We partner with trusted operators to improve field efficiency and return capital to investors through quarterly distributions.</p>
    <p>Our fund acquires producing oil and gas assets with steady cash flow and low decline rates. We partner with trusted operators to improve field efficiency and return capital to investors through quarterly distributions.</p>
  </div>
  <div class="copy" style="left:149px;top:35px;width:117px">
    <p>Our fund acquires producing oil and gas assets with steady cash flow and low decline rates. We partner with trusted operators to improve field efficiency and return capital to investors through quarterly distributions. Our fund acquires producing oil and gas assets with steady cash flow and low decline rates. We partner with trusted operators to improve field efficiency and return capital to investors through quarterly distributions.</p>
    <p>Our fund acquires producing oil and gas assets with steady cash flow and low decline rates. We partner with trusted operators to improve field efficiency and return capital to investors through quarterly distributions. Our fund acquires producing oil and gas assets with steady cash flow and low decline rates. We partner with trusted operators to improve field efficiency and return capital to investors through quarterly distributions.</p>
    <p>Our fund acquires producing oil and gas assets with steady cash flow and low decline rates. We partner with trusted operators to improve field efficiency and return capital to investors through quarterly distributions.</p>
  </div>
  <div class="footer"></div><p class="footer-note">Page: 11 &nbsp;|&nbsp; Harrow Ridge presentation to: Company Investor</p><p class="footer-brand"><i></i>HARROW RIDGE</p>
</section>

<!-- 12 Three columns -->
<section class="slide">
  <div class="accent"></div>
  <h2 class="title">Text in Three Columns With Sub Header</h2>
  <p class="subhead">Lorem ipsum, giving information on its origins, as well as a random text here</p>
  <div class="copy" style="left:21px;top:35px;width:76px">
    <p>Our fund acquires producing oil and gas assets with steady cash flow and low decline rates. We partner with trusted operators to improve field efficiency and return capital to investors through quarterly distributions. Our fund acquires producing oil and gas assets with steady cash flow and low decline rates. We partner with trusted operators to improve field efficiency and return capital to investors through quarterly distributions.</p>
    <p>Our fund acquires producing oil and gas assets with steady cash flow and low decline rates. We partner with trusted operators to improve field efficiency and return capital to investors through quarterly distributions. Our fund acquires producing oil and gas assets with steady cash flow and low decline rates. We partner with trusted operators to improve field efficiency and return capital to investors through quarterly distributions.</p>
  </div>
  <div class="copy" style="left:105px;top:35px;width:76px">
    <p>Our fund acquires producing oil and gas assets with steady cash flow and low decline rates. We partner with trusted operators to improve field efficiency and return capital to investors through quarterly distributions. Our fund acquires producing oil and gas assets with steady cash flow and low decline rates. We partner with trusted operators to improve field efficiency and return capital to investors through quarterly distributions.</p>
    <p>Our fund acquires producing oil and gas assets with steady cash flow and low decline rates. We partner with trusted operators to improve field efficiency and return capital to investors through quarterly distributions. Our fund acquires producing oil and gas assets with steady cash flow and low decline rates. We partner with trusted operators to improve field efficiency and return capital to investors through quarterly distributions.</p>
  </div>
  <div class="copy" style="left:189px;top:35px;width:76px">
    <p>Our fund acquires producing oil and gas assets with steady cash flow and low decline rates. We partner with trusted operators to improve field efficiency and return capital to investors through quarterly distributions. Our fund acquires producing oil and gas assets with steady cash flow and low decline rates. We partner with trusted operators to improve field efficiency and return capital to investors through quarterly distributions.</p>
    <p>Our fund acquires producing oil and gas assets with steady cash flow and low decline rates. We partner with trusted operators to improve field efficiency and return capital to investors through quarterly distributions. Our fund acquires producing oil and gas assets with steady cash flow and low decline rates. We partner with trusted operators to improve field efficiency and return capital to investors through quarterly distributions.</p>
  </div>
  <div class="footer"></div><p class="footer-note">Page: 12 &nbsp;|&nbsp; Harrow Ridge presentation to: Company Investor</p><p class="footer-brand"><i></i>HARROW RIDGE</p>
</section>

<!-- 13 Six icon bullets -->
<section class="slide">
  <div class="accent"></div>
  <h2 class="title">Six Bullet Icon slide With Sub Header</h2>
  <p class="subhead">Lorem ipsum, giving information on its origins, as well as a random text here</p>
  <div class="icon-item" style="left:23px;top:38px"><svg width="17" height="17" viewBox="0 0 17 17"><circle cx="8.5" cy="8.5" r="8.5" fill="#bdbdbd"/><path d="M5 11.5V9h1.5v2.5zM7.8 11.5V7h1.5v4.5zM10.5 11.5V5H12v6.5z" fill="#fff"/></svg><h3>Your subtitle here</h3><p>Steady cash flow from producing wells.</p></div>
  <div class="icon-item" style="left:108px;top:38px"><svg width="17" height="17" viewBox="0 0 17 17"><circle cx="8.5" cy="8.5" r="8.5" fill="#9a9a9a"/><circle cx="8.5" cy="8.5" r="3.2" fill="none" stroke="#fff" stroke-width="1.4"/><path d="M5 5.5h7" stroke="#fff" stroke-width="1"/></svg><h3>Your subtitle here</h3><p>Steady cash flow from producing wells.</p></div>
  <div class="icon-item" style="left:193px;top:38px"><svg width="17" height="17" viewBox="0 0 17 17"><circle cx="8.5" cy="8.5" r="8.5" fill="#555"/><path d="M5.5 12h6l-3-7z" fill="none" stroke="#fff" stroke-width="1.1"/></svg><h3>Your subtitle here</h3><p>Steady cash flow from producing wells.</p></div>
  <div class="icon-item" style="left:23px;top:87px"><svg width="17" height="17" viewBox="0 0 17 17"><circle cx="8.5" cy="8.5" r="8.5" fill="#8a8a8a"/><path d="M8.5 4L6 12.5h5zM6.8 9.5h3.4" fill="none" stroke="#fff" stroke-width="1"/></svg><h3>Your subtitle here</h3><p>Steady cash flow from producing wells.</p></div>
  <div class="icon-item" style="left:108px;top:87px"><svg width="17" height="17" viewBox="0 0 17 17"><circle cx="8.5" cy="8.5" r="8.5" fill="#666"/><rect x="5" y="5.5" width="7" height="6" fill="none" stroke="#fff" stroke-width="1"/><path d="M7 11.5V8.5M9 11.5V7.5M11 11.5V9" stroke="#fff" stroke-width=".8"/></svg><h3>Your subtitle here</h3><p>Steady cash flow from producing wells.</p></div>
  <div class="icon-item" style="left:193px;top:87px"><svg width="17" height="17" viewBox="0 0 17 17"><circle cx="8.5" cy="8.5" r="8.5" fill="#2b2b2b"/><path d="M5 5v7M5 8.5h3M8 5v7M10 6.5h2.5M11.2 5.5v6.5" stroke="#fff" stroke-width="1"/></svg><h3>Your subtitle here</h3><p>Steady cash flow from producing wells.</p></div>
  <div class="footer"></div><p class="footer-note">Page: 13 &nbsp;|&nbsp; Harrow Ridge presentation to: Company Investor</p><p class="footer-brand"><i></i>HARROW RIDGE</p>
</section>

<!-- 14 Six numbered bullets -->
<section class="slide">
  <div class="accent"></div>
  <h2 class="title">Six Bullet slide With Sub Header</h2>
  <p class="subhead">Lorem ipsum, giving information on its origins, as well as a random text here</p>
  <div class="num-item" style="left:22px;top:46px"><h3><em>01</em>Your subtitle here</h3><p>Steady cash flow from producing wells across mature basins.</p></div>
  <div class="num-item" style="left:108px;top:46px"><h3><em>02</em>Your subtitle here</h3><p>Steady cash flow from producing wells across mature basins.</p></div>
  <div class="num-item" style="left:194px;top:46px"><h3><em>03</em>Your subtitle here</h3><p>Steady cash flow from producing wells across mature basins.</p></div>
  <div class="num-item" style="left:24px;top:92px"><h3><em>04</em>Your subtitle here</h3><p>Steady cash flow from producing wells across mature basins.</p></div>
  <div class="num-item" style="left:110px;top:92px"><h3><em>05</em>Your subtitle here</h3><p>Steady cash flow from producing wells across mature basins.</p></div>
  <div class="num-item" style="left:196px;top:92px"><h3><em>06</em>Your subtitle here</h3><p>Steady cash flow from producing wells across mature basins.</p></div>
  <div class="footer"></div><p class="footer-note">Page: 14 &nbsp;|&nbsp; Harrow Ridge presentation to: Company Investor</p><p class="footer-brand"><i></i>HARROW RIDGE</p>
</section>

<!-- 15 Four options -->
<section class="slide">
  <div class="accent"></div>
  <h2 class="title">Four Options slide</h2>
  <p class="subhead">Lorem ipsum, giving information on its origins, as well as a random text here</p>
  <div class="option" style="left:35px"><strong>01</strong><p>Steady cash flow from producing wells across mature basins.</p></div>
  <div class="option dim" style="left:90px"><strong>02</strong><p>Steady cash flow from producing wells across mature basins.</p></div>
  <div class="option dim" style="left:145px"><strong>03</strong><p>Steady cash flow from producing wells across mature basins.</p></div>
  <div class="option dim" style="left:200px"><strong>04</strong><p>Steady cash flow from producing wells across mature basins.</p></div>
  <p class="option-btn on" style="left:35px">Option name</p>
  <p class="option-btn" style="left:90px">Option name</p>
  <p class="option-btn" style="left:145px">Option name</p>
  <p class="option-btn" style="left:200px">Option name</p>
  <div class="footer"></div><p class="footer-note">Page: 15 &nbsp;|&nbsp; Harrow Ridge presentation to: Company Investor</p><p class="footer-brand"><i></i>HARROW RIDGE</p>
</section>

<!-- 16 Bar chart -->
<section class="slide">
  <div class="accent"></div>
  <h2 class="title">Data with descriptive text Slide</h2>
  <p class="subhead">Lorem ipsum, giving information on its origins, as well as a random text here</p>
  <svg style="left:22px;top:35px" width="245" height="80" viewBox="0 0 245 80">
    <text class="chart-label" x="122" y="4" text-anchor="middle">Chart Title</text>
    <g stroke="#e6e6e6" stroke-width=".4"><path d="M15 8.2H240M15 16H240M15 23.8H240M15 31.6H240M15 39.4H240M15 47.2H240M15 55H240"/></g>
    <g class="chart-label" text-anchor="end"><text x="10" y="9">6</text><text x="10" y="17">5</text><text x="10" y="25">4</text><text x="10" y="32">3</text><text x="10" y="40">2</text><text x="10" y="48">1</text><text x="10" y="56">0</text></g>
    <g fill="#d8d8d8"><rect x="23" y="21.5" width="9" height="33.5"/><rect x="79" y="35.5" width="9" height="19.5"/><rect x="135" y="27.7" width="9" height="27.3"/><rect x="191" y="19.9" width="9" height="35.1"/></g>
    <g fill="#b0b0b0"><rect x="34" y="36.3" width="9" height="18.7"/><rect x="90" y="20.7" width="9" height="34.3"/><rect x="146" y="41" width="9" height="14"/><rect x="202" y="33.2" width="9" height="21.8"/></g>
    <g fill="#8a8a8a"><rect x="45" y="32.4" width="9" height="22.6"/><rect x="101" y="41" width="9" height="14"/><rect x="157" y="37.8" width="9" height="17.2"/><rect x="213" y="33.2" width="9" height="21.8"/></g>
    <g fill="#666"><rect x="56" y="39.4" width="9" height="15.6"/><rect x="112" y="33.2" width="9" height="21.8"/><rect x="168" y="31.6" width="9" height="23.4"/><rect x="224" y="16" width="9" height="39"/></g>
    <g class="chart-label" text-anchor="middle"><text x="44" y="61">Category 1</text><text x="100" y="61">Category 2</text><text x="156" y="61">Category 3</text><text x="212" y="61">Category 4</text></g>
    <g class="chart-label"><rect x="80" y="67" width="2" height="2" fill="#d8d8d8"/><text x="83.5" y="69">Series 1</text><rect x="100" y="67" width="2" height="2" fill="#b0b0b0"/><text x="103.5" y="69">Series 2</text><rect x="120" y="67" width="2" height="2" fill="#8a8a8a"/><text x="123.5" y="69">Series 22</text><rect x="142" y="67" width="2" height="2" fill="#666"/><text x="145.5" y="69">Series 3</text></g>
  </svg>
  <p class="copy" style="left:24px;top:121px;width:240px;font-size:3px;line-height:4.3px">Our fund acquires producing oil and gas assets with steady cash flow and low decline rates. We partner with trusted operators to improve field efficiency and return capital to investors through quarterly distributions.</p>
  <div class="footer"></div><p class="footer-note">Page: 16 &nbsp;|&nbsp; Harrow Ridge presentation to: Company Investor</p><p class="footer-brand"><i></i>HARROW RIDGE</p>
</section>

<!-- 17 Line chart -->
<section class="slide">
  <div class="accent"></div>
  <h2 class="title">Data with descriptive text Slide</h2>
  <p class="subhead">Lorem ipsum, giving information on its origins, as well as a random text here</p>
  <svg style="left:18px;top:36px" width="132" height="98" viewBox="0 0 132 98">
    <text class="chart-label" x="70" y="4" text-anchor="middle">Chart Title</text>
    <g stroke="#ececec" stroke-width=".4"><path d="M14 8H126M14 18.7H126M14 29.3H126M14 40H126M14 50.7H126M14 61.3H126M14 72H126"/></g>
    <g class="chart-label" text-anchor="end"><text x="9" y="9">6</text><text x="9" y="20">5</text><text x="9" y="30">4</text><text x="9" y="41">3</text><text x="9" y="52">2</text><text x="9" y="62">1</text><text x="9" y="73">0</text></g>
    <g fill="none" stroke-width=".8">
      <path d="M28 26 56 45 84 35 112 24" stroke="#bbb"/>
      <path d="M28 45 56 25 84 53 112 42" stroke="#222"/>
      <path d="M28 50 56 53 84 48 112 38" stroke="#888"/>
      <path d="M28 57 56 52 84 45 112 20" stroke="#666"/>
    </g>
    <g class="chart-label" text-anchor="middle"><text x="28" y="78">Category 1</text><text x="56" y="78">Category 2</text><text x="84" y="78">Category 3</text><text x="112" y="78">Category 4</text></g>
    <g class="chart-label" stroke-width=".6"><path d="M30 89h4" stroke="#bbb"/><text x="35" y="90">Series 1</text><path d="M49 89h4" stroke="#222"/><text x="54" y="90">Series 2</text><path d="M68 89h4" stroke="#888"/><text x="73" y="90">Series 22</text><path d="M89 89h4" stroke="#666"/><text x="94" y="90">Series 3</text></g>
  </svg>
  <div style="left:164px;top:37px;width:102px">
    <h3 style="font:400 4.6px 'Roboto Condensed',sans-serif;color:var(--ink);margin-bottom:3px">Your subtitle slide here</h3>
    <p class="copy" style="font-size:3px;line-height:3.9px;color:#333">Our fund acquires producing oil and gas assets with steady cash flow and low decline rates. We partner with trusted operators to improve field efficiency and return capital to investors through quarterly distributions.</p>
    <div style="margin-top:4px">
      <div class="list-item"><em>1</em><p>Steady cash flow from producing wells across mature basins.</p></div>
      <div class="list-item"><em>2</em><p>Steady cash flow from producing wells across mature basins.</p></div>
      <div class="list-item"><em>3</em><p>Steady cash flow from producing wells across mature basins.</p></div>
      <div class="list-item"><em>4</em><p>Steady cash flow from producing wells across mature basins.</p></div>
    </div>
  </div>
  <div class="footer"></div><p class="footer-note">Page: 17 &nbsp;|&nbsp; Harrow Ridge presentation to: Company Investor</p><p class="footer-brand"><i></i>HARROW RIDGE</p>
</section>

<!-- 18 Comparison -->
<section class="slide">
  <div class="accent"></div>
  <h2 class="title">Data Comparison with descriptive text Slide</h2>
  <p class="subhead">Lorem ipsum, giving information on its origins, as well as a random text here</p>
  <svg style="left:44px;top:29px" width="76" height="52" viewBox="0 0 76 52">
    <text class="chart-label" x="38" y="4" text-anchor="middle" style="font-size:3.6px">Sales</text>
    <g transform="rotate(-90 38 23)" fill="none" stroke-width="3.6">
      <circle cx="38" cy="23" r="14" stroke="#ddd"/>
      <circle cx="38" cy="23" r="14" stroke="#111" stroke-dasharray="51 37"/>
      <circle cx="38" cy="23" r="14" stroke="#999" stroke-dasharray="20 68" stroke-dashoffset="-51"/>
      <circle cx="38" cy="23" r="14" stroke="#bbb" stroke-dasharray="9 79" stroke-dashoffset="-71"/>
    </g>
    <g class="chart-label" style="font-size:2.3px"><text x="12" y="48">▪ 1st Qtr</text><text x="27" y="48">▪ 2nd Qtr</text><text x="43" y="48">▪ 3rd Qtr</text><text x="58" y="48">▪ 4th Qtr</text></g>
  </svg>
  <svg style="left:172px;top:27px" width="76" height="52" viewBox="0 0 76 52">
    <text class="chart-label" x="38" y="4" text-anchor="middle" style="font-size:3.6px">Sales</text>
    <g transform="rotate(-90 38 23)" fill="none" stroke-width="3.6">
      <circle cx="38" cy="23" r="14" stroke="#ddd"/>
      <circle cx="38" cy="23" r="14" stroke="#111" stroke-dasharray="53 35"/>
      <circle cx="38" cy="23" r="14" stroke="#999" stroke-dasharray="18 70" stroke-dashoffset="-53"/>
      <circle cx="38" cy="23" r="14" stroke="#bbb" stroke-dasharray="10 78" stroke-dashoffset="-71"/>
    </g>
    <g class="chart-label" style="font-size:2.3px"><text x="12" y="48">▪ 1st Qtr</text><text x="27" y="48">▪ 2nd Qtr</text><text x="43" y="48">▪ 3rd Qtr</text><text x="58" y="48">▪ 4th Qtr</text></g>
  </svg>
  <div style="left:24px;top:83px;width:102px">
    <p class="copy" style="font-size:2.6px;line-height:3.3px">Our fund acquires producing oil and gas assets with steady cash flow and low decline rates. We partner with trusted operators to improve field efficiency and return capital to investors through quarterly distributions.</p>
    <div class="list-item"><em>1</em><p>Steady cash flow from producing wells across mature basins.</p></div>
    <div class="list-item"><em>2</em><p>Steady cash flow from producing wells across mature basins.</p></div>
    <div class="list-item"><em>3</em><p>Steady cash flow from producing wells across mature basins.</p></div>
    <div class="list-item"><em>4</em><p>Steady cash flow from producing wells across mature basins.</p></div>
  </div>
  <div style="left:152px;top:82px;width:102px">
    <p class="copy" style="font-size:2.6px;line-height:3.3px">Our fund acquires producing oil and gas assets with steady cash flow and low decline rates. We partner with trusted operators to improve field efficiency and return capital to investors through quarterly distributions.</p>
    <div class="list-item"><em>1</em><p>Steady cash flow from producing wells across mature basins.</p></div>
    <div class="list-item"><em>2</em><p>Steady cash flow from producing wells across mature basins.</p></div>
    <div class="list-item"><em>3</em><p>Steady cash flow from producing wells across mature basins.</p></div>
    <div class="list-item"><em>4</em><p>Steady cash flow from producing wells across mature basins.</p></div>
  </div>
  <div class="footer"></div><p class="footer-note">Page: 18 &nbsp;|&nbsp; Harrow Ridge presentation to: Company Investor</p><p class="footer-brand"><i></i>HARROW RIDGE</p>
</section>

</main>
</body>
</html>
```